DL SIZED ONE SIDED BROCHURE FOR CLEANING AND GARDENING SERVICE

business name: K&T property services
services provided: Strata cleaning,lawn mowing,hedge trimming,garden maintainance,lawn repair,weed spraying/removal, rubbish removal.
10 years experience and fully insured.
obligation free quotes.
phone number:contact doug 0427391054
email: ktpropertyservices@mailvane.example
slogan: when quality matters ring K&T
K&T logo would be nice but not essential
DL size in inches: 3.9in × 8.2in
DL size in millimetres: 100mm × 210mm
DL size in centimetres: 10cm x 21cm
Updates
doing good guys no suggestions except being original
Target Market(s)
real estate agents, private home owners, contractors.
Industry/Entity Type
Business
Look and feel
Each slider illustrates characteristics of the customer's brand and the style your logo design should communicate.

```html
<!DOCTYPE html>
<html lang="en">
<head>
<meta charset="utf-8">
<title>K&amp;T Property Services – DL Brochure</title>
<link rel="stylesheet" href="https://fonts.googleapis.com/css2?family=Open+Sans:wght@700;800&display=swap">
<style>
  :root {
    --leaf: #97c655;
    --leaf-soft: #b4cf8c;
    --leaf-deep: #7aae45;
    --sun: #f8a54d;
    --paper: #ffffff;
    --ink: #111111;
  }
  * { margin: 0; padding: 0; box-sizing: border-box; }
  html, body { width: 1200px; height: 2608px; overflow: hidden; background: var(--leaf); }
  .brochure {
    position: relative;
    width: 1200px;
    height: 2608px;
    overflow: hidden;
    font-family: "Open Sans", Arial, sans-serif;
    font-weight: 700;
    color: var(--paper);
  }
  .backdrop { position: absolute; inset: 0; }
  .brand-name {
    position: absolute;
    left: 72px;
    top: 140px;
    font-size: 76px;
    font-weight: 800;
    letter-spacing: 1px;
    line-height: 1;
    white-space: nowrap;
  }
  .brand-name .initials { font-size: 106px; }
  .slogan {
    position: absolute;
    right: 72px;
    top: 300px;
    font-size: 49px;
    line-height: 1;
    white-space: nowrap;
  }
  .service-list {
    position: absolute;
    left: 322px;
    top: 1292px;
    list-style: none;
  }
  .service-list li {
    display: flex;
    align-items: center;
    height: 100px;
    font-size: 58px;
    line-height: 1;
    white-space: nowrap;
  }
  .service-list svg { width: 46px; height: 46px; margin-right: 26px; flex: none; }
  .contact-box {
    position: absolute;
    left: 300px;
    top: 2036px;
    width: 620px;
    height: 192px;
    background: var(--paper);
    border: 4px solid var(--ink);
    color: var(--ink);
    text-align: center;
    display: flex;
    flex-direction: column;
    justify-content: center;
    line-height: 1.1;
  }
  .contact-box .contact-name { font-size: 62px; }
  .contact-box .contact-phone { font-size: 68px; }
  .credentials {
    position: absolute;
    left: 0;
    width: 1200px;
    top: 2282px;
    text-align: center;
    font-size: 47px;
    letter-spacing: 1px;
    white-space: nowrap;
  }
  .credentials .years { font-size: 64px; }
  .offer {
    position: absolute;
    left: 0;
    width: 1200px;
    top: 2392px;
    text-align: center;
    font-size: 70px;
    letter-spacing: 1px;
    line-height: 1.1;
    white-space: nowrap;
  }
  .email {
    position: absolute;
    left: 0;
    width: 1200px;
    top: 2518px;
    text-align: center;
    font-size: 36px;
    line-height: 1;
    white-space: nowrap;
  }
</style>
</head>
<body>
<main class="brochure">
  <svg class="backdrop" width="1200" height="2608" viewBox="0 0 1200 2608">
    <defs>
      <linearGradient id="hero-tone" x1="0" y1="0" x2="0" y2="1">
        <stop offset="0" stop-color="var(--leaf-soft)"/>
        <stop offset="1" stop-color="var(--leaf-deep)"/>
      </linearGradient>
    </defs>
    <rect width="1200" height="2608" fill="var(--leaf)"/>
    <rect class="hero-photo" x="0" y="380" width="1200" height="880" fill="url(#hero-tone)" role="img" aria-label="Photo of a brick bungalow with hedges, a paved path and a freshly mown front lawn"/>
    <path d="M0,430 C300,380 700,500 1200,420 L1200,370 L0,370Z" fill="var(--leaf)"/>
    <path d="M0,430 C300,380 700,500 1200,420 L1200,462 C700,540 300,422 0,472Z" fill="var(--paper)"/>
    <path d="M0,1170 C400,1240 800,1120 1200,1190 L1200,1232 C800,1162 400,1282 0,1212Z" fill="var(--paper)"/>
    <path d="M0,1212 C400,1282 800,1162 1200,1232 L1200,1270 L0,1270Z" fill="var(--leaf)"/>
    <path d="M0,2095 C400,2045 800,2115 1200,2065 L1200,2608 L0,2608Z" fill="var(--sun)" stroke="var(--paper)" stroke-width="10"/>
  </svg>

  <h1 class="brand-name"><span class="initials">K&amp;T</span> PROPERTY SERVICES</h1>
  <p class="slogan">when quality matters ring K&amp;T</p>

  <ul class="service-list">
    <li><svg viewBox="0 0 24 24"><path d="M3 13l6 6L21 5" fill="none" stroke="#fff" stroke-width="3.5" stroke-linecap="round" stroke-linejoin="round"/></svg>strata cleaning</li>
    <li><svg viewBox="0 0 24 24"><path d="M3 13l6 6L21 5" fill="none" stroke="#fff" stroke-width="3.5" stroke-linecap="round" stroke-linejoin="round"/></svg>lawn mowing</li>
    <li><svg viewBox="0 0 24 24"><path d="M3 13l6 6L21 5" fill="none" stroke="#fff" stroke-width="3.5" stroke-linecap="round" stroke-linejoin="round"/></svg>hedge trimming</li>
    <li><svg viewBox="0 0 24 24"><path d="M3 13l6 6L21 5" fill="none" stroke="#fff" stroke-width="3.5" stroke-linecap="round" stroke-linejoin="round"/></svg>fertilizing</li>
    <li><svg viewBox="0 0 24 24"><path d="M3 13l6 6L21 5" fill="none" stroke="#fff" stroke-width="3.5" stroke-linecap="round" stroke-linejoin="round"/></svg>lawn repair</li>
    <li><svg viewBox="0 0 24 24"><path d="M3 13l6 6L21 5" fill="none" stroke="#fff" stroke-width="3.5" stroke-linecap="round" stroke-linejoin="round"/></svg>weed spraying/removal</li>
    <li><svg viewBox="0 0 24 24"><path d="M3 13l6 6L21 5" fill="none" stroke="#fff" stroke-width="3.5" stroke-linecap="round" stroke-linejoin="round"/></svg>rubbish removal</li>
  </ul>

  <div class="contact-box">
    <span class="contact-name">contact Doug</span>
    <span class="contact-phone">0427391054</span>
  </div>

  <p class="credentials"><span class="years">10</span> YEARS EXPERIENCE AND FULLY INSURED</p>
  <p class="offer">OBLIGATION FREE QUOTES</p>
  <p class="email">ktpropertyservices@mailvane.example</p>
</main>
</body>
</html>
```